依頼詳細
お客様にわかりやすく、またチラシをみてポイントカードを持っておきたい、もらっておきたいと思わせるデザインを希望します。お客様の目に入りやすく、A1のポスターや、レジ横でA4の用紙に置く予定です。
内容はジュース1杯で1P
10Pでお好きなドリンク1杯サービスです!(どのサイズでも)
入会費、年会費無料、有効期限なし!
記載項目
ポイントカード
サイズ
A4
ページ数
片面
希望イメージ
シンプル 複雑
単色 カラフル
暗い 明るい
日常 高級
遊び心 厳粛
未来的 伝統的
女性的 男性的
希望する色
黄・オレンジ系
納品ファイル
• 高解像度JPG (.jpg)
補足説明
参考イメージ添付します。
依頼公開後の追記内容
ポイントカード画像を添付します。
■ 選んだ理由

ポイントカードが目立つ

■ 提案者全員のお礼・コメント

どれもレベルが高い提案で選ぶことが難しかったです。また機会がございましたらよろしくお願いします。

```html
<!DOCTYPE html>
<html lang="ja">
<head>
<meta charset="utf-8">
<title>お得なポイントカード</title>
<link href="https://fonts.googleapis.com/css2?family=M+PLUS+Rounded+1c:wght@500;700;800;900&display=swap" rel="stylesheet">
<style>
  :root{
    --bg-yellow:#fdc923;
    --white:#ffffff;
    --cream:#fdf4e3;
    --brown:#6b3a1e;
    --red:#e33a2a;
    --orange:#f08a12;
    --pink:#e9708a;
    --grey:#d9d4cc;
  }
  html,body{margin:0;padding:0;overflow:hidden;}
  body{width:851px;height:1200px;}
  .poster{
    position:relative;width:851px;height:1200px;overflow:hidden;
    background:var(--bg-yellow);
    font-family:"M PLUS Rounded 1c",sans-serif;color:var(--brown);
  }
  .headline-plate{
    position:absolute;left:130px;top:0;width:591px;height:170px;
    background:var(--white);border-radius:0 0 40px 40px;
  }
  .headline-lead{
    position:absolute;left:0;top:34px;width:851px;text-align:center;
    font-size:76px;font-weight:900;color:var(--red);letter-spacing:2px;line-height:100px;
  }
  .headline-lead .spark{display:inline-block;width:10px;height:52px;background:var(--red);border-radius:5px;vertical-align:middle;margin:0 30px;}
  .headline-lead .spark.l{transform:rotate(-25deg);}
  .headline-lead .spark.r{transform:rotate(25deg);}
  .headline-main{
    position:absolute;left:0;top:140px;width:851px;margin:0;text-align:center;
    font-size:100px;font-weight:900;color:var(--white);line-height:130px;white-space:nowrap;
    -webkit-text-stroke:9px var(--brown);paint-order:stroke fill;letter-spacing:2px;
  }
  .info-panel{
    position:absolute;left:36px;top:278px;width:767px;height:562px;
    background:var(--cream);border:6px solid var(--brown);border-radius:8px;
  }
  .info-panel::after{
    content:"";position:absolute;inset:10px;border:2px dashed #c9a77f;border-radius:4px;
  }
  .card{
    position:absolute;background:var(--white);border-radius:6px;
    box-shadow:4px 6px 0 var(--grey);
  }
  .card.back{left:305px;top:335px;width:245px;height:215px;transform:rotate(2deg);}
  .card.front{left:60px;top:345px;width:255px;height:170px;z-index:2;}
  .card-title{position:absolute;left:24px;top:62px;font-size:24px;font-weight:700;color:#333;white-space:nowrap;}
  .rate-tag{
    position:absolute;left:336px;top:282px;width:145px;height:74px;z-index:3;
    background:var(--white);border:3px solid var(--brown);border-radius:14px;
    transform:rotate(-8deg);text-align:center;
    font-size:24px;font-weight:800;line-height:30px;padding-top:6px;box-sizing:border-box;white-space:nowrap;
  }
  .free-note{
    position:absolute;left:572px;top:300px;width:232px;margin:0;text-align:center;
    font-size:30px;font-weight:900;color:var(--red);line-height:42px;white-space:nowrap;
    transform:rotate(-6deg);
  }
  .badge{
    position:absolute;left:44px;top:580px;width:128px;height:128px;z-index:3;
    border-radius:50%;background:var(--white);border:9px solid var(--orange);
    box-sizing:border-box;text-align:center;
  }
  .badge-num{display:block;margin-top:20px;font-size:38px;font-weight:900;color:var(--brown);line-height:42px;}
  .badge-sub{display:block;font-size:15px;font-weight:700;white-space:nowrap;}
  .reward{position:absolute;left:200px;top:588px;width:400px;text-align:center;z-index:3;}
  .reward-item{display:block;font-size:38px;font-weight:900;color:var(--brown);line-height:50px;white-space:nowrap;}
  .reward-offer{display:block;font-size:38px;font-weight:900;color:var(--orange);line-height:50px;white-space:nowrap;}
  .reward-size{
    display:inline-block;margin-top:10px;padding:2px 22px;
    border:3px solid var(--pink);border-radius:30px;background:var(--white);
    font-size:24px;font-weight:800;color:var(--pink);white-space:nowrap;
  }
  .juice-photo{
    position:absolute;left:604px;top:540px;width:196px;height:262px;z-index:2;
    border-radius:10px 10px 40px 40px;
    background:linear-gradient(180deg,#fbd36b 0%,#f5a623 45%,#ec8a14 100%);
  }
  .mango-photo{
    position:absolute;left:20px;top:872px;width:811px;height:310px;
    border-radius:140px;
    background:linear-gradient(90deg,#e5482a 0%,#f28a2a 35%,#f7a43a 60%,#f8b53b 100%);
  }
</style>
</head>
<body>
<main class="poster">
  <div class="headline-plate"></div>
  <div class="headline-lead"><span class="spark l"></span>お得な!<span class="spark r"></span></div>
  <h1 class="headline-main">ポイントカード</h1>

  <section class="info-panel"></section>
  <div class="card back"></div>
  <div class="card front"><span class="card-title">ポイントカード</span></div>
  <div class="rate-tag">ジュース<br>1杯で1P</div>
  <p class="free-note">入会費、<br>年会費無料、<br>有効期限<br>なし!</p>

  <div class="badge"><span class="badge-num">10P</span><span class="badge-sub">たまると…</span></div>
  <div class="reward">
    <span class="reward-item">お好きなドリンク</span>
    <span class="reward-offer">1杯サービスです!</span>
    <span class="reward-size">どのサイズでもOK!</span>
  </div>
  <div class="juice-photo" role="img" aria-label="カップに入ったマンゴージュースの写真"></div>

  <div class="mango-photo" role="img" aria-label="丸ごとのマンゴー2個とカットしたマンゴーの写真"></div>
</main>
</body>
</html>
```